We are wanting a designer to design an ebook on Residential Property in Australia. This ebook is a quarterly report and covers 5 major capital cities in Australia. This is the first quarterly report for the year - another 3 are needed to be created. If you are chosen as our designer please expect ongoing work which is well rewarded.

To begin with:

We will only need you to design a few pages so we can see your style. Then if you are chosen we will get you to do the whole thing.

Can you please design the title page, page 5 and the Adelaide section(page 6 & 7) of the The Suburban Dwelling Forecast - Seasonal Capital Briefing - Q1 2014 document attached.

The ebook brief:

You will need to create 2 graphs to include in the ebook from the data I give to you for each capital city (one graph for houses and one graph for units).

We already have a style of ebook in mind from a previous ebook our in-office designer has created for our company. You will need to keep with the logo/style/colours/fonts etc. We are looking for a designer based in Australia.

Sources and content:

Below I have shared a dropbox folder with you. It contains the first ebook our designer has created for you to view the style,logo etc - YieldHaven-Property-ebook. The folder also contains the source files for the logo.

https://www.filecrate-share.com/sh/k4p2xq7vb9rm3d/BXQ581zt/

The Suburban Dwelling Forecast - Seasonal Capital Briefing - Q1 2014 document attached is the content we need made into the ebook.

Each page has been set out with the content needed for that page. Each capital city content spreads out over two pages with a graph on each. I have highlighted in red the data needed to create each of the graphs. The graph style must look like the Sector Horizon image in the shared dropbox folder.

You will also need to redesign the graph on page 5. You may do this how you like as long as it keeps in the style of the ebook. We will also need the source files on this ebook.

```html
<!DOCTYPE html>
<html lang="en">
<head>
<meta charset="utf-8">
<title>Adelaide – South Australia</title>
<link rel="stylesheet" href="https://fonts.googleapis.com/css2?family=Montserrat:wght@400;600;700&display=swap">
<style>
  :root {
    --brand-red: #b0242b;
    --text-grey: #555555;
    --ink: #1a1a1a;
    --grid: #dddddd;
    --white: #ffffff;
  }
  * { margin: 0; padding: 0; box-sizing: border-box; }
  html, body { width: 849px; height: 1200px; overflow: hidden; background: var(--white); }
  body { font-family: "Montserrat", Arial, sans-serif; color: var(--text-grey); position: relative; }

  .hero-photo {
    position: absolute; left: 0; top: 0; width: 849px; height: 520px;
    background: linear-gradient(180deg, #9fb4c6 0%, #c7d2da 12%, #3a3430 16%, #a0683e 30%, #6e3a22 48%, #c9a27a 62%, #e7d8c4 78%, #bf8d5c 100%);
  }
  .hero-band { position: absolute; left: 0; top: 520px; width: 849px; height: 45px; background: var(--brand-red); }

  .section-title { position: absolute; left: 44px; top: 614px; font-size: 23px; font-weight: 700; color: var(--brand-red); letter-spacing: 0.3px; }
  .section-title .region { font-weight: 400; font-size: 18px; }

  .intro { position: absolute; left: 44px; top: 664px; width: 760px; font-size: 14.2px; line-height: 1.22; }
  .intro h2 { font-size: 14.2px; font-weight: 700; color: var(--text-grey); margin-bottom: 19px; }
  .intro p { margin-bottom: 19px; }

  .outlook-box {
    position: absolute; left: 44px; top: 898px; width: 279px; height: 258px;
    background: var(--brand-red); color: var(--white); padding: 14px 28px 0 21px;
    font-size: 10.8px; line-height: 11.6px; overflow: hidden;
  }
  .outlook-box h3 { font-size: 10.8px; font-weight: 700; }
  .outlook-box ul { list-style: none; margin-bottom: 12px; }
  .outlook-box li { padding-left: 10px; text-indent: -10px; }
  .outlook-box li::before { content: "• "; }

  .chart { position: absolute; left: 338px; top: 896px; }
  .chart text { font-family: "Montserrat", Arial, sans-serif; }

  .page-number { position: absolute; right: 44px; top: 1170px; font-size: 11px; color: var(--ink); }
  .page-number b { font-weight: 700; }
</style>
</head>
<body>
  <div class="hero-photo" role="img" aria-label="Photograph of a modern two-storey home with timber cladding, a balcony and garden plants at dusk"></div>
  <div class="hero-band"></div>

  <h1 class="section-title">ADELAIDE <span class="region">SOUTH AUSTRALIA</span></h1>

  <div class="intro">
    <h2>Adelaide in review</h2>
    <p>The property market in South Australia is performing well and The Southern Realty Council (SRC) anticipate that positive growth for the state will continue into 2014.</p>
    <p>Looking at median house price data for the previous 12 months, Adelaide showed an encouraging increase of 2.8 per cent with the median house price now sitting at $407,500. According to SRC President, Mr Len Marlow, “This is the first time in almost three years that the median price has crossed the $400,000 threshold.”</p>
    <p>Adelaide's unit market is also up by 2.56 per cent with a current median value of $305,000</p>
  </div>

  <aside class="outlook-box">
    <h3>Adelaide Sector Horizon – Houses Median Values of Adelaide over the quarter to March 31 2014.</h3>
    <ul>
      <li>There were 17,226 house sales in Adelaide during the last year.</li>
      <li>Capital growth in the Adelaide housing market over the last year was 4.55% and the Adelaide median house value is now $407,500.</li>
      <li>The Adelaide house median rental yield is 4.66% and the median weekly rent is $365.</li>
    </ul>
    <p>Median Value: $407,500<br>Capital Growth: 2.65% 2%+ pa next 5 yrs<br>Number of sales: 5,059<br>Rental yield: 4.66%<br>Median rent: $365<br>Total return: 1.87%</p>
  </aside>

  <svg class="chart" width="470" height="250" viewBox="338 896 470 250" aria-label="Line chart of median value of Adelaide houses, Dec 2003 to Dec 2013">
    <line x1="340" y1="912" x2="806" y2="912" stroke="#1a1a1a" stroke-width="2"/>
    <rect x="440" y="898" width="262" height="29" fill="#1a1a1a"/>
    <text x="571" y="918" fill="#ffffff" font-size="13" text-anchor="middle">Median Value - Adelaide  Houses</text>

    <g stroke="#dddddd" stroke-width="1">
      <line x1="410" y1="953" x2="775" y2="953"/><line x1="410" y1="972" x2="775" y2="972"/>
      <line x1="410" y1="990" x2="775" y2="990"/><line x1="410" y1="1009" x2="775" y2="1009"/>
      <line x1="410" y1="1027" x2="775" y2="1027"/><line x1="410" y1="1046" x2="775" y2="1046"/>
      <line x1="410" y1="1064" x2="775" y2="1064"/><line x1="410" y1="1083" x2="775" y2="1083"/>
      <line x1="410" y1="1101" x2="775" y2="1101"/>
    </g>
    <line x1="410" y1="1120" x2="775" y2="1120" stroke="#999999" stroke-width="1"/>

    <g fill="#1a1a1a" font-size="11" text-anchor="end">
      <text x="405" y="957">$450,000</text><text x="405" y="976">$400,000</text>
      <text x="405" y="994">$350,000</text><text x="405" y="1013">$300,000</text>
      <text x="405" y="1031">$250,000</text><text x="405" y="1050">$200,000</text>
      <text x="405" y="1068">$150,000</text><text x="405" y="1087">$100,000</text>
      <text x="405" y="1105">$50,000</text><text x="405" y="1124">$0</text>
    </g>

    <g fill="#555555">
      <circle cx="415" cy="1120" r="1.6"/><circle cx="433" cy="1120" r="1.6"/><circle cx="451" cy="1120" r="1.6"/>
      <circle cx="469" cy="1120" r="1.6"/><circle cx="486" cy="1120" r="1.6"/><circle cx="504" cy="1120" r="1.6"/>
      <circle cx="522" cy="1120" r="1.6"/><circle cx="540" cy="1120" r="1.6"/><circle cx="558" cy="1120" r="1.6"/>
      <circle cx="576" cy="1120" r="1.6"/><circle cx="594" cy="1120" r="1.6"/><circle cx="611" cy="1120" r="1.6"/>
      <circle cx="629" cy="1120" r="1.6"/><circle cx="647" cy="1120" r="1.6"/><circle cx="665" cy="1120" r="1.6"/>
      <circle cx="683" cy="1120" r="1.6"/><circle cx="701" cy="1120" r="1.6"/><circle cx="718" cy="1120" r="1.6"/>
      <circle cx="736" cy="1120" r="1.6"/><circle cx="754" cy="1120" r="1.6"/><circle cx="772" cy="1120" r="1.6"/>
    </g>

    <g fill="#1a1a1a" font-size="6.2" text-anchor="middle">
      <text x="415" y="1134">Dec</text><text x="433" y="1134">Jun</text><text x="451" y="1134">Dec</text>
      <text x="469" y="1134">Jun</text><text x="486" y="1134">Dec</text><text x="504" y="1134">Jun</text>
      <text x="522" y="1134">Dec</text><text x="540" y="1134">Jun</text><text x="558" y="1134">Dec</text>
      <text x="576" y="1134">Jun</text><text x="594" y="1134">Dec</text><text x="611" y="1134">Jun</text>
      <text x="629" y="1134">Dec</text><text x="647" y="1134">Jun</text><text x="665" y="1134">Dec</text>
      <text x="683" y="1134">Jun</text><text x="701" y="1134">Dec</text><text x="718" y="1134">Jun</text>
      <text x="736" y="1134">Dec</text><text x="754" y="1134">Jun</text><text x="772" y="1134">Dec</text>
      <text x="415" y="1143">2003</text><text x="433" y="1143">2004</text><text x="451" y="1143">2004</text>
      <text x="469" y="1143">2005</text><text x="486" y="1143">2005</text><text x="504" y="1143">2006</text>
      <text x="522" y="1143">2006</text><text x="540" y="1143">2007</text><text x="558" y="1143">2007</text>
      <text x="576" y="1143">2008</text><text x="594" y="1143">2008</text><text x="611" y="1143">2009</text>
      <text x="629" y="1143">2009</text><text x="647" y="1143">2010</text><text x="665" y="1143">2010</text>
      <text x="683" y="1143">2011</text><text x="701" y="1143">2011</text><text x="718" y="1143">2012</text>
      <text x="736" y="1143">2012</text><text x="754" y="1143">2013</text><text x="772" y="1143">2013</text>
    </g>

    <polyline fill="none" stroke="#b0242b" stroke-width="1.6" stroke-linejoin="round"
      points="415,1027 424,1024 433,1022 442,1020 451,1019 460,1017 469,1016 478,1014 486,1014 495,1013 504,1011 513,1009 522,1009 531,1005 540,1001 549,993 558,986 567,981 576,981 585,980 594,977 603,977 611,973 620,970 629,968 638,968 647,965 656,965 665,964 674,966 683,968 692,970 701,971 710,972 718,973 727,973 736,972 745,972 754,970 763,969 772,967"/>
  </svg>

  <div class="page-number"><b>7</b> | Page</div>
</body>
</html>
```